Designer and consultant for professionals/businesses and manufacturers in the kitchen and bath in...

I have 30 years of design experience, and 19 of those years within the marketing team of a national cabinet manufacturer. This role gave me the opportunity to consult and design for kitchen/bath businesses, from boutique to multi-store national scale. My services include layout and spatial planning, individual display design, and product design for cabinet manufacturers. From showrooms, to trade shows to integrated design collections. I would like to see designs that convey professionalism, as well as an appeal to the creative designer mind!

Target Market(s)

Kitchen and bath dealers, as well as mid-scale multi-store home centers. Cabinet manufacturers, Trade Show agencies.

Industry/Entity Type

Kitchen

Contact Information for Business Card

Serving Kitchen and Bath Businesses

Logo Text

MT (initials for business name)

Font styles to use
Serif
Sans Serif
Decorative

Colors
e34197

Requirements
Must have
• Marlowe Tavish Design and Consulting, Inc. (business name)
• marlowe@mtvantra.com (email)
• 917-555-0148 (phone)
• mtvantra.com (website)
Nice to have
• Inclusions of geometric shapes; particularly a 30/15 degree triangle and circle(s)
• 2 colors
Should not have
• Not too artsy!

```html
<!DOCTYPE html>
<html lang="en">
<head>
<meta charset="utf-8">
<title>Marlowe Tavish Design and Consulting, Inc. – Business Card</title>
<link rel="stylesheet" href="https://fonts.googleapis.com/css2?family=Raleway:wght@400;500;600;700&display=swap">
<style>
  :root {
    --charcoal: #3d3e40;
    --blush: #f7c4c4;
    --blush-text: #f2b7b5;
    --paper: #ffffff;
    --ink: #3a3a3c;
    --backdrop: #d3d4d3;
  }
  * { margin: 0; padding: 0; box-sizing: border-box; }
  html, body {
    width: 1200px; height: 900px; overflow: hidden;
    background: var(--backdrop);
    font-family: "Raleway", Arial, sans-serif;
  }
  .stage {
    width: 1200px; height: 900px;
    display: flex; flex-direction: column;
    align-items: center; justify-content: center; gap: 56px;
  }
  .card {
    position: relative;
    width: 630px; height: 360px;
    box-shadow: 0 6px 18px rgba(0,0,0,0.18);
    overflow: hidden;
  }
  /* Front */
  .card--front {
    background: var(--charcoal);
    display: flex; align-items: center; justify-content: center;
  }
  .brand { display: flex; align-items: center; gap: 16px; }
  .brand__dot {
    width: 46px; height: 46px; border-radius: 50%;
    border: 2px solid var(--blush);
    flex: none;
  }
  .brand__text { display: flex; flex-direction: column; }
  .brand__name {
    font-weight: 600; font-size: 34px; letter-spacing: 0.2px;
    color: var(--blush-text); line-height: 1.1;
  }
  .brand__sub {
    font-weight: 500; font-size: 17px; letter-spacing: 0.6px;
    line-height: 1.4;
  }
  .card--front .brand__sub { color: #e8e8e8; }

  /* Back */
  .card--back { background: var(--paper); }
  .card__shapes { position: absolute; inset: 0; }
  .tagline {
    position: absolute; top: 30px; right: 150px;
    text-align: right;
    font-weight: 500; font-size: 22px; line-height: 1.3;
    color: var(--blush-text);
  }
  .card--back .brand { position: absolute; left: 70px; top: 196px; }
  .card--back .brand__name { font-size: 30px; }
  .card--back .brand__sub { color: var(--ink); font-size: 15px; }
  .contact {
    position: absolute; left: 70px; top: 286px;
    font-size: 14px; font-weight: 500; color: var(--ink);
    display: grid; grid-template-columns: auto auto; column-gap: 22px; row-gap: 10px;
  }
  .contact__item { display: flex; align-items: center; gap: 7px; }
  .contact__icon { width: 15px; height: 15px; flex: none; }
  .contact__web { grid-column: 2; letter-spacing: 0.5px; }
  .contact__web strong { color: var(--blush-text); font-weight: 600; }
</style>
</head>
<body>
<main class="stage">
  <section class="card card--front" aria-label="Card front">
    <div class="brand">
      <span class="brand__dot"></span>
      <div class="brand__text">
        <span class="brand__name">Marlowe Tavish</span>
        <span class="brand__sub">Design &amp; Consulting, Inc.</span>
      </div>
    </div>
  </section>

  <section class="card card--back" aria-label="Card back">
    <svg class="card__shapes" width="630" height="360" viewBox="0 0 630 360" aria-hidden="true">
      <polygon points="0,0 470,0 500,165 0,190" fill="var(--charcoal)"/>
      <polygon points="482,0 630,0 630,262" fill="var(--blush)"/>
    </svg>
    <p class="tagline">Serving<br>Kitchen &amp; Bath<br>Business</p>

    <div class="brand">
      <span class="brand__dot"></span>
      <div class="brand__text">
        <span class="brand__name">Marlowe Tavish</span>
        <span class="brand__sub">Design &amp; Consulting, Inc.</span>
      </div>
    </div>

    <div class="contact">
      <span class="contact__item">
        <svg class="contact__icon" viewBox="0 0 16 16"><circle cx="8" cy="8" r="8" fill="var(--blush)"/><path d="M5.3 4.2l1.4-.2.8 1.9-1 .8a5.5 5.5 0 0 0 2.8 2.8l.8-1 1.9.8-.2 1.4c-3.6.3-6.8-2.9-6.5-6.5z" fill="#fff"/></svg>
        917-555-0148
      </span>
      <span class="contact__item">
        <svg class="contact__icon" viewBox="0 0 16 16"><circle cx="8" cy="8" r="8" fill="var(--blush)"/><rect x="4" y="5.2" width="8" height="5.6" rx="0.6" fill="none" stroke="#fff" stroke-width="1.1"/><path d="M4.3 5.6L8 8.4l3.7-2.8" fill="none" stroke="#fff" stroke-width="1.1"/></svg>
        mtvantra@postline.com
      </span>
      <span class="contact__web">www.<strong>mtvantra</strong>.com</span>
    </div>
  </section>
</main>
</body>
</html>
```